Business card for job seeker professional

Hi. I'm a sale and marketing professional who's just moved to Australia and looking for a job. I would like to have a business card designed for me, which I can use for job interviews/networking. Given Pravolink increasing importance in the job market, I would like my public profile link (http://au.pravolink-net.com/in/tomasveridun/) to be incorporated into my details.

```html
<!DOCTYPE html>
<html lang="en">
<head>
<meta charset="utf-8">
<title>Tomas Veridun – Business Card</title>
<link rel="stylesheet" href="https://fonts.googleapis.com/css2?family=Libre+Baskerville:wght@700&display=swap">
<style>
  :root {
    --backdrop: #e6e7e8;
    --card: #ffffff;
    --band-dark: #1b66a0;
    --band-light: #3a9fdc;
    --label-blue: #1f6aa5;
    --ink: #111111;
    --white: #ffffff;
  }
  * { box-sizing: border-box; margin: 0; padding: 0; }
  html, body {
    width: 1200px; height: 1000px; overflow: hidden;
    background: var(--backdrop);
    font-family: "Libre Baskerville", Georgia, serif;
  }
  .card {
    position: absolute; left: 250px; top: 298px;
    width: 698px; height: 403px;
    background: var(--card);
    border-radius: 36px;
    overflow: hidden;
  }
  .name-band {
    position: absolute; left: 0; top: 170px; width: 100%; height: 84px;
    border-top: 5px solid var(--band-dark);
    border-bottom: 4px solid var(--band-dark);
  }
  .name-band__fill {
    position: absolute; left: 0; right: 0; top: 3px; bottom: 3px;
    background: linear-gradient(90deg, var(--band-light) 0%, var(--band-dark) 22%, var(--band-dark) 78%, var(--band-light) 100%);
    display: flex; align-items: center; justify-content: center;
  }
  .holder-name {
    color: var(--white); font-size: 42px; font-weight: 700; letter-spacing: 0;
  }
  .contacts {
    position: absolute; left: 0; top: 276px; width: 100%;
    text-align: center; font-size: 17px; font-weight: 700; line-height: 31px;
  }
  .contact-line { display: flex; justify-content: center; align-items: center; gap: 3px; white-space: nowrap; }
  .contact-label { color: var(--label-blue); }
  .contact-value { color: var(--ink); }
  .contact-link { color: var(--label-blue); margin-left: 8px; }
  .contact-icon { width: 20px; height: 20px; }
  .network-name { color: var(--ink); }
</style>
</head>
<body>
  <div class="card">
    <div class="name-band">
      <div class="name-band__fill">
        <h1 class="holder-name">Tomas Veridun</h1>
      </div>
    </div>
    <div class="contacts">
      <p class="contact-line">
        <span class="contact-label">Email</span>
        <svg class="contact-icon" viewBox="0 0 20 20" aria-hidden="true">
          <path d="M2 8 L10 2 L18 8 V18 H2 Z" fill="var(--band-light)"/>
          <path d="M2 8 L10 13 L18 8" fill="none" stroke="#fff" stroke-width="1.5"/>
          <path d="M2 18 L8 12 M18 18 L12 12" stroke="#fff" stroke-width="1.2"/>
        </svg>
        <span class="contact-value">example-mail@examplesite.com</span>
      </p>
      <p class="contact-line">
        <span class="contact-label">Mobile</span>
        <svg class="contact-icon" viewBox="0 0 20 20" aria-hidden="true">
          <path d="M4 2 L7 2 L8.5 6 L6.5 7.5 C7.5 10 10 12.5 12.5 13.5 L14 11.5 L18 13 L18 16 C18 17 17 18 16 18 C8.5 17.5 2.5 11.5 2 4 C2 3 3 2 4 2 Z" fill="var(--band-light)"/>
        </svg>
        <span class="contact-value">0000 000 000</span>
      </p>
      <p class="contact-line">
        <span class="network-name">Pravolink</span>
        <span class="contact-link">http://au.pravolink-net.com/in/tomasveridun/</span>
      </p>
    </div>
  </div>
</body>
</html>
```